Business Card Design Project

Hi,

We are a new modern sheet metal business and I require a business card for our sales reps.

The card should be double sided and standout in a crowd.

I have attached our logo and our website is www.folvik.com.au.

Please ask if you have any further questions
Updates

hi everyone, 

I'm wondering if we can try to lighten the cards mood.  Everyone is using black and I'm not sure how that would be accepted in real life.

Gregory

Reason: Still No receiving what I was hoping for.

Industry/Entity Type

Business

Requirements
Must have
• double sided

```html
<!DOCTYPE html>
<html lang="en">
<head>
<meta charset="utf-8">
<title>Folvik Sheetmetal – Business Card</title>
<link href="https://fonts.googleapis.com/css2?family=Jost:wght@400;500;700&display=swap" rel="stylesheet">
<style>
  :root {
    --backdrop: #3b3d40;
    --navy: #0c1528;
    --navy-edge: #070d1a;
    --brand-blue: #1f4f9e;
    --silver-light: #e6e8ea;
    --silver-mid: #c9cdd1;
    --silver-dark: #b3b8bd;
    --ink: #2a2e33;
    --tag-grey: #a9b0bb;
    --white: #ffffff;
  }
  * { box-sizing: border-box; margin: 0; padding: 0; }
  html, body {
    width: 1200px; height: 900px; overflow: hidden;
    background: var(--backdrop);
    font-family: "Jost", Arial, sans-serif;
  }
  .canvas {
    width: 1200px; height: 900px;
    display: flex; flex-direction: column;
    align-items: center; justify-content: center; gap: 50px;
  }
  .card {
    width: 620px; height: 378px;
    position: relative;
    overflow: hidden;
    box-shadow: 0 14px 32px rgba(0,0,0,0.45);
  }

  /* Front side */
  .card--front {
    background: radial-gradient(ellipse at 50% 45%, #15203a 0%, var(--navy) 55%, var(--navy-edge) 100%);
    display: flex; flex-direction: column; align-items: center; justify-content: center;
    padding: 0 48px;
  }
  .brand {
    display: flex; align-items: center; gap: 14px;
    white-space: nowrap;
  }
  .brand__square {
    flex: none;
    width: 26px; height: 26px; background: var(--brand-blue);
  }
  .brand__name {
    font-weight: 700; letter-spacing: 1px; line-height: 1;
  }
  .card--front .brand__name { color: var(--white); font-size: 40px; }
  .tagline {
    margin-top: 24px; font-size: 18px; color: var(--tag-grey); letter-spacing: 0.3px;
    white-space: nowrap;
  }
  .tagline .divider { color: var(--brand-blue); margin: 0 8px; }

  /* Back side */
  .card--back {
    background:
      repeating-linear-gradient(100deg, rgba(255,255,255,0.08) 0 2px, rgba(0,0,0,0.03) 2px 5px),
      linear-gradient(160deg, var(--silver-light) 0%, var(--silver-mid) 45%, var(--silver-dark) 100%);
    color: var(--ink);
  }
  .contact {
    position: absolute; left: 40px; top: 42px;
  }
  .contact__name {
    color: var(--brand-blue); font-size: 20px; font-weight: 500;
    text-transform: uppercase; letter-spacing: 0.5px;
  }
  .contact__role { font-size: 14px; margin-bottom: 12px; }
  .contact__line { font-size: 13px; line-height: 1.55; }
  .contact__label { color: var(--brand-blue); display: inline-block; width: 16px; }

  .card--back .brand { position: absolute; right: 40px; top: 132px; gap: 10px; }
  .card--back .brand__name { color: var(--brand-blue); font-size: 28px; }
  .card--back .brand__square { width: 18px; height: 18px; }
  .card--back .tagline {
    position: absolute; right: 40px; top: 172px; margin: 0;
    font-size: 13px; color: var(--ink);
  }
  .address {
    position: absolute; right: 40px; bottom: 42px;
    text-align: right; font-size: 15px; line-height: 1.45; font-style: normal;
  }
</style>
</head>
<body>
<main class="canvas">
  <section class="card card--front" aria-label="Card front">
    <div class="brand">
      <span class="brand__square"></span>
      <span class="brand__name">FOLVIK SHEETMETAL</span>
    </div>
    <p class="tagline">Flashings<span class="divider">|</span>Gutter<span class="divider">|</span>Rainwater Goods</p>
  </section>

  <section class="card card--back" aria-label="Card back">
    <div class="contact">
      <p class="contact__name">Daniel Harrow</p>
      <p class="contact__role">Managing Director</p>
      <p class="contact__line"><span class="contact__label">p</span>3705 2140</p>
      <p class="contact__line"><span class="contact__label">f</span>3288 6710</p>
      <p class="contact__line"><span class="contact__label">e</span>info@folvik.com.au</p>
      <p class="contact__line"><span class="contact__label">w</span>www.folvik.com.au</p>
    </div>
    <div class="brand">
      <span class="brand__square"></span>
      <span class="brand__name">FOLVIK SHEETMETAL</span>
    </div>
    <p class="tagline">Flashings<span class="divider">|</span>Gutter<span class="divider">|</span>Rainwater Goods</p>
    <address class="address">
      22 Quarry Street Redbank Q 4301<br>
      PO Box 318 Redbank Q 4301
    </address>
  </section>
</main>
</body>
</html>
```